Financial Advisor / Asset Manager Zup Design

I'm currently hosting with Zup and my first attempt at a website is live at www.ravenholtwealth.example Clearly I am not a web designer and I need help making this more catchy, modern, cross-platform compatible, search engine optimized, etc. I've got logos, hex color pallets, and a slew of other graphics. I'm interested in working with a winning designer to write/refine my copy/language to complete the build.

Full set of graphics https://pics.lumora-share.example/q71TzR05KwPd2MhXN do NOT use the CONSULTING graphics as this is for a related business / different website

Target Market(s)

Individuals, small institutions, endowments, non-profits seeking financial advice and asset / portfolio management

Industry/Entity Type

Financial Services

Coding

Coded - Design and coding required

Font styles to use
Other font styles liked:
• AvenirLTStd - Black, Book, and Roman as appropriate

Requirements
Must have
• Complete, cross platform website integrating my existing logo
Nice to have
• Easy to update format for go-forward maintenance

```html
<!DOCTYPE html>
<html lang="en">
<head>
<meta charset="utf-8">
<title>Ravenholt Wealth</title>
<link href="https://fonts.googleapis.com/css2?family=Lato:wght@300;400;700;900&display=swap" rel="stylesheet">
<style>
:root{
  --blue:#1b6cc4;
  --blue-dark:#1459a8;
  --blue-light:#1f93e4;
  --ink:#222;
  --muted:#555;
  --faq-bg:#f1f3f6;
  --white:#fff;
  --black:#000;
}
*{box-sizing:border-box;margin:0;padding:0}
html,body{width:1200px;height:4060px;overflow:hidden}
body{font-family:'Lato',sans-serif;color:var(--ink);background:var(--white);position:relative}
.abs{position:absolute}

/* hero */
.hero-bg{left:0;top:0;width:1200px;height:690px;
  background:linear-gradient(180deg,#3a4c63 0%,#5b6b72 35%,#6f7560 60%,#5d6148 100%);
  clip-path:polygon(0 0,1200px 0,1200px 440px,1100px 455px,1000px 500px,900px 525px,820px 565px,750px 605px,690px 650px,640px 688px,570px 640px,500px 612px,420px 580px,330px 545px,250px 520px,170px 480px,80px 465px,0 420px)}
.logo-text{color:var(--white);font-weight:400;font-size:24px;letter-spacing:1px;line-height:1}
.logo-text small{display:block;font-size:12px;letter-spacing:3px;margin-top:4px;text-align:center}
.nav{left:468px;top:34px;display:flex;gap:31px;font-size:13px;font-weight:700;color:var(--white)}
.nav .active{border-bottom:2px solid var(--white);padding-bottom:6px}
.phone-btn{left:897px;top:21px;width:170px;height:46px;border:2px solid var(--white);color:var(--white);font-weight:700;font-size:16px;display:flex;align-items:center;justify-content:center;gap:7px}
.hero-kicker{left:0;width:1200px;top:190px;text-align:center;color:var(--white);font-size:19px;letter-spacing:6px}
.hero-title{left:0;width:1200px;top:226px;text-align:center;color:var(--white);font-size:64px;font-weight:300;letter-spacing:1px}
.hero-text{left:170px;width:860px;top:310px;text-align:center;color:var(--white);font-size:13px;line-height:28px}
.btn{display:flex;align-items:center;justify-content:center;font-weight:900;font-size:16px}
.hero-btn{left:515px;top:383px;width:170px;height:45px;background:var(--white);color:var(--blue)}
.dots{left:574px;top:560px;display:flex;gap:4px}
.dots i{width:9px;height:9px;border-radius:50%;background:var(--white)}
.dots i:first-child{background:var(--blue-light)}

/* who */
.bull{left:130px;top:730px;width:385px;height:300px;border-radius:40% 50% 30% 40%;
  background:radial-gradient(ellipse at 50% 55%,#9fc6ee 0%,#d7e8f8 60%,#fff 100%)}
.h2{color:var(--blue);font-weight:400;font-size:37px}
.h2::after{content:"";display:block;width:68px;height:3px;background:var(--blue);margin-top:12px}
.center .h2::after,.h2.center::after{margin-left:auto;margin-right:auto}
.who-title{left:598px;top:738px}
.who-text{left:598px;top:815px;width:470px;font-size:13px;line-height:28px;text-align:justify;color:#333}
.who-link{left:598px;top:968px;width:480px;font-size:14px;line-height:28px;font-weight:700;color:var(--blue)}
.values-bg{left:0;top:1040px;width:1200px;height:322px;background:linear-gradient(180deg,#fff 0%,#e6edf4 30%,#c9d5e0 70%,#aebdca 100%)}
.value{width:206px;height:206px;top:1068px;border-radius:50%;display:flex;flex-direction:column;align-items:center;justify-content:center;color:var(--white);font-size:16px;text-align:center;line-height:24px}
.value svg{margin-bottom:14px}
.value.dark{background:var(--blue-dark)}
.value.light{background:var(--blue-light)}

/* offer */
.offer{left:0;top:1362px;width:1200px;height:660px;background:linear-gradient(180deg,#1764c0 0%,#1a6dcb 60%,#2474cf 100%)}
.offer-title{left:0;width:1200px;top:1440px;text-align:center}
.offer-title .h2{color:var(--white)}
.offer-title .h2::after{background:var(--white)}
.card{top:1532px;width:303px;height:402px;background:var(--white);padding:5px;text-align:center}
.card .photo{height:212px}
.card h3{font-weight:400;font-size:19px;margin-top:22px;color:#111}
.card p{font-size:12.5px;line-height:28px;color:#333;padding:0 12px;margin-top:3px}
.card a{display:inline-block;margin-top:8px;font-size:13px;font-weight:700;color:var(--blue);text-decoration:underline}

/* faq */
.faq-title{left:0;width:1200px;top:2098px;text-align:center}
.faq-item{left:165px;width:870px;height:52px;border-radius:10px;background:var(--faq-bg);display:flex;align-items:center;justify-content:space-between;padding:0 30px 0 22px;font-size:13px;font-weight:700;color:#222}
.faq-item.open{background:var(--blue);color:var(--white)}
.faq-answer{left:190px;top:2258px;width:810px;font-size:12.5px;line-height:25.5px;color:#333}
.faq-answer span{color:var(--blue)}

/* contact */
.touch-bg{left:0;top:2870px;width:1200px;height:900px;background:linear-gradient(180deg,#fff 0%,#f2f4f7 25%,#dfe5ea 55%,#c8d1d9 100%)}
.touch-title{left:0;width:1200px;top:2952px;text-align:center}
.field{height:48px;border:1.5px solid #666;background:var(--white);font-size:12px;color:#666;padding:14px 19px}
.submit{left:515px;top:3405px;width:170px;height:47px;background:var(--blue);color:var(--white)}

/* footer */
.ridge{left:0;top:3555px}
.footer-logo{left:130px;top:3845px;color:var(--blue);font-size:29px;font-weight:400;letter-spacing:1px;text-align:center;width:195px;line-height:1}
.footer-logo small{display:block;font-size:15px;letter-spacing:4px;margin-top:6px}
.f-head{color:var(--white);font-weight:900;font-size:15px}
.f-list{color:var(--white);font-size:13px;list-style:none}
.f-list li{line-height:28px}
.f-list li::before{content:"»";margin-right:14px}
.c-row{display:flex;align-items:center;gap:14px;color:var(--white);font-size:13px;line-height:28px}
.c-ico{width:28px;height:28px;border-radius:50%;background:var(--blue);flex:none;display:flex;align-items:center;justify-content:center}
.news-text{color:var(--white);font-size:13px;line-height:28px}
.news-input{left:800px;top:3868px;width:202px;height:38px;background:var(--white);font-size:11px;color:#888;padding:11px 12px}
.news-send{left:1002px;top:3868px;width:52px;height:38px;background:var(--blue);display:flex;align-items:center;justify-content:center}
.social{width:28px;height:28px;border-radius:50%;background:var(--blue)}
.rule{left:120px;top:3986px;width:960px;height:1px;background:#666}
.copy{left:0;width:1200px;top:4010px;text-align:center;color:var(--white);font-size:11.5px}
</style>
</head>
<body>

<!-- Hero -->
<div class="abs hero-bg" role="img" aria-label="Alpine mountain range with rocky peaks and a mountain hut"></div>
<div class="abs logo-text" style="left:135px;top:24px">RAVENHOLT WEALTH<small>— CAPITAL —</small></div>
<nav class="abs nav"><span class="active">HOME</span><span>ABOUT</span><span>FAQS</span><span>SERVICES</span><span>CONTACT</span></nav>
<div class="abs phone-btn"><svg width="16" height="16" viewBox="0 0 24 24" fill="#fff"><path d="M6.6 10.8a15.1 15.1 0 0 0 6.6 6.6l2.2-2.2c.3-.3.7-.4 1-.2 1.1.4 2.3.6 3.6.6.6 0 1 .4 1 1V20c0 .6-.4 1-1 1C10.6 21 3 13.4 3 4c0-.6.4-1 1-1h3.5c.6 0 1 .4 1 1 0 1.3.2 2.5.6 3.6.1.3 0 .7-.2 1z"/></svg>(555) 014-2290</div>
<div class="abs hero-kicker">WELCOME TO</div>
<h1 class="abs hero-title">RAVENHOLT WEALTH</h1>
<p class="abs hero-text">Ravenholt Wealth is for investors looking for the attention and personalization of services typically reserved for ultra high net worth (UHNW) investors. Our founder served UHNW clients at Halvard Bank, Northmere Partners, and Brightwater &amp; Co. for over 15 years.</p>
<div class="abs btn hero-btn">GET STARTED</div>
<div class="abs dots"><i></i><i></i><i></i><i></i></div>

<!-- Who we are -->
<div class="abs bull" role="img" aria-label="Blue line illustration of a bull and bear over a candlestick chart"></div>
<h2 class="abs h2 who-title">WHO WE ARE</h2>
<p class="abs who-text">Ravenholt Wealth is an investment advisory firm committed to serving as fiduciary to our clients. We always act in the best interests of our clients, including putting your interests ahead of our own. We provide independent financial planning, investment management, and asset management services tailored to your unique needs and circumstances.</p>
<p class="abs who-link">COME TO RAVENHOLT WEALTH AND FIND OUT HOW WE CAN DO BETTER TOGETHER</p>

<div class="abs values-bg" role="img" aria-label="Faded snowy mountain range"></div>
<div class="abs value dark" style="left:133px">
  <svg width="92" height="92" viewBox="0 0 92 92" fill="none" stroke="#fff" stroke-width="3"><circle cx="46" cy="46" r="42"/><path d="M46 16v30l18 18"/></svg>
  YOU COME FIRST</div>
<div class="abs value light" style="left:376px">
  <svg width="84" height="80" viewBox="0 0 84 80" fill="none" stroke="#fff" stroke-width="3"><circle cx="36" cy="40" r="14"/><path d="M14 40a22 22 0 0 1 44 0M12 36v12M60 36v12M16 66c6-8 34-8 40 0"/><rect x="54" y="6" width="26" height="18" rx="3"/></svg>
  PERSONALIZED<br>SERVICES</div>
<div class="abs value dark" style="left:619px">
  <svg width="84" height="80" viewBox="0 0 84 80" fill="none" stroke="#fff" stroke-width="3"><rect x="34" y="8" width="40" height="26" rx="3" transform="rotate(-30 54 21)"/><circle cx="54" cy="22" r="6"/><path d="M6 56l16-10h18l12 6-14 6H26M6 56l10 16 30-6 28-20"/></svg>
  TRANSPARENT<br>FEES</div>
<div class="abs value light" style="left:862px">
  <svg width="84" height="84" viewBox="0 0 84 84" fill="none" stroke="#fff" stroke-width="3"><circle cx="42" cy="42" r="9"/><circle cx="16" cy="16" r="7"/><circle cx="68" cy="16" r="9"/><circle cx="16" cy="68" r="7"/><circle cx="68" cy="68" r="7"/><path d="M22 22l12 12M62 24l-12 12M22 62l12-12M62 62l-12-12"/></svg>
  WE GIVE BACK</div>

<!-- What we offer -->
<div class="abs offer" role="img" aria-label="Blue tinted mountain backdrop"></div>
<div class="abs offer-title"><h2 class="h2 center">WHAT WE OFFER</h2></div>
<div class="abs card" style="left:131px">
  <div class="photo" role="img" aria-label="Team reviewing financial charts at a desk" style="background:linear-gradient(135deg,#c9a57a,#7c6a58 55%,#3f4c5c)"></div>
  <h3>STOCK SELECTION</h3>
  <p>Many advisors use a screening process to find investments. You may be familiar with stock screening as many websites.</p>
  <a>LEARN MORE</a>
</div>
<div class="abs card" style="left:449px">
  <div class="photo" role="img" aria-label="Laptop with floating finance icons" style="background:linear-gradient(135deg,#3b4148,#1e2226 60%,#5a6068)"></div>
  <h3>ALTERNATIVE INVESTMENTS</h3>
  <p>The challenges facing investors seeking to build portfolios capable of generating attractive returns with acceptable .</p>
  <a>LEARN MORE</a>
</div>
<div class="abs card" style="left:766px">
  <div class="photo" role="img" aria-label="Hand writing beside a laptop with gear graphics" style="background:linear-gradient(135deg,#e6eef6,#9fbcd8 55%,#3b6fa6)"></div>
  <h3>OPTIMIZATION</h3>
  <p>Your investment portfolio was built with money you earned. It should be customized to reflect your goals and tailored.</p>
  <a>LEARN MORE</a>
</div>

<!-- FAQ -->
<div class="abs faq-title"><h2 class="h2 center">FREQUENTLY ASKED QUESTIONS</h2></div>
<div class="abs faq-item open" style="top:2195px">WHAT IS A REGISTERED INVESTMENT ADVISOR? ARE YOU A REGISTERED INVESTMENT ADVISOR?<span>+</span></div>
<p class="abs faq-answer">A registered investment advisor (RIA) is a company or individual that provides financial advice to its clients and is registered with a regulatory authority, either the Federal Securities Board (FSB) or state securities administrators. All RIAs can be looked up on the Adviser Public Register (APR) website. You can find us on the APR website at <span>https://www.adviser-register.example/firm/204118.</span></p>
<div class="abs faq-item" style="top:2387px">WHAT DOES BEING AN INDEPENDENT FINANCIAL ADVISOR MEAN? WHY DOES IT MATTER?<span>+</span></div>
<div class="abs faq-item" style="top:2459px">WHAT IS A FIDUCIARY? ARE YOU A FIDUCIARY?<span>+</span></div>
<div class="abs faq-item" style="top:2531px">WHAT IS A CUSTODIAN? ARE YOU A CUSTODIAN?<span>+</span></div>
<div class="abs faq-item" style="top:2603px">WHAT ARE YOUR FEES? HOW MUCH WILL I PAY?<span>+</span></div>
<div class="abs faq-item" style="top:2670px">HOW OFTEN WILL WE MEET? HOW WILL YOU KEEP ME INFORMED?<span>+</span></div>
<div class="abs faq-item" style="top:2741px">I ALREADY HAVE AN ADVISOR. WHY SHOULD I BOTHER SWITCHING? THAT'S SO MUCH WORK!<span>+</span></div>

<!-- Contact -->
<div class="abs touch-bg" role="img" aria-label="Misty faded mountain landscape"></div>
<div class="abs touch-title"><h2 class="h2 center">GET IN TOUCH</h2></div>
<div class="abs field" style="left:300px;top:3048px;width:292px">First Name</div>
<div class="abs field" style="left:607px;top:3048px;width:293px">Last Name</div>
<div class="abs field" style="left:300px;top:3113px;width:600px">Email Address</div>
<div class="abs field" style="left:300px;top:3177px;width:292px">Phone Number</div>
<div class="abs field" style="left:607px;top:3177px;width:293px">Subject</div>
<div class="abs field" style="left:300px;top:3242px;width:600px;height:120px">Message</div>
<div class="abs btn submit">SUBMIT NOW</div>

<!-- Footer -->
<svg class="abs ridge" width="1200" height="505" viewBox="0 0 1200 505">
  <polygon fill="#3a3a3a" points="0,230 150,150 260,120 330,80 420,40 460,70 520,20 600,0 660,30 740,60 820,50 900,100 1000,130 1100,200 1200,260 1200,505 0,505"/>
  <polygon fill="#000" points="0,250 120,185 230,160 330,110 420,75 470,100 530,55 600,30 660,62 740,92 830,85 910,130 1010,160 1110,225 1200,280 1200,505 0,505"/>
</svg>
<div class="abs footer-logo">RAVENHOLT<br>WEALTH<small>— CAPITAL —</small></div>

<div class="abs f-head" style="left:368px;top:3772px">QUICK LINKS</div>
<ul class="abs f-list" style="left:368px;top:3800px"><li>Home</li><li>About</li><li>FAQs</li><li>Services</li><li>Contact</li></ul>

<div class="abs f-head" style="left:537px;top:3772px">CONTACT US</div>
<div class="abs c-row" style="left:535px;top:3804px"><span class="c-ico"><svg width="12" height="14" viewBox="0 0 24 28" fill="#fff"><path d="M12 0a10 10 0 0 0-10 10c0 8 10 18 10 18s10-10 10-18A10 10 0 0 0 12 0zm0 14a4 4 0 1 1 0-8 4 4 0 0 1 0 8z"/></svg></span><span>2208 Alder Ridge Rd, Suite #40<br>Fernhollow, VA 20000</span></div>
<div class="abs c-row" style="left:535px;top:3872px"><span class="c-ico"><svg width="12" height="12" viewBox="0 0 24 24" fill="#fff"><path d="M6.6 10.8a15.1 15.1 0 0 0 6.6 6.6l2.2-2.2c.3-.3.7-.4 1-.2 1.1.4 2.3.6 3.6.6.6 0 1 .4 1 1V20c0 .6-.4 1-1 1C10.6 21 3 13.4 3 4c0-.6.4-1 1-1h3.5c.6 0 1 .4 1 1 0 1.3.2 2.5.6 3.6.1.3 0 .7-.2 1z"/></svg></span><span>(555) 014-2290</span></div>
<div class="abs c-row" style="left:535px;top:3926px"><span class="c-ico"><svg width="13" height="10" viewBox="0 0 26 20" fill="#fff"><path d="M0 0h26v3L13 11 0 3zM0 6l13 8 13-8v14H0z"/></svg></span><span>info@ravenholtwealth.example</span></div>

<div class="abs f-head" style="left:798px;top:3772px">SIGN UP FOR OUR NEWSLETTER</div>
<p class="abs news-text" style="left:800px;top:3800px;width:260px">Lorem ipsum dolor sit amet, consectet ur adipiscing elit, sed do.</p>
<div class="abs news-input">Enter The Email</div>
<div class="abs news-send"><svg width="18" height="16" viewBox="0 0 24 22" fill="#fff"><path d="M0 10L24 0 19 22 12 15 20 5 9 13z"/></svg></div>
<div class="abs social" style="left:803px;top:3925px"></div>
<div class="abs social" style="left:847px;top:3925px"></div>
<div class="abs social" style="left:891px;top:3925px"></div>
<div class="abs social" style="left:935px;top:3925px"></div>

<div class="abs rule"></div>
<div class="abs copy">© Copyrights 2022 &nbsp;Ravenholt Wealth LLC &nbsp;| &nbsp;&nbsp;All Rights Reserved</div>

</body>
</html>
```